Hypnosis signage

I need a signage 3.50 mt width x 1.60 length.
I'm attaching a signage.
But few changes the Text in the center slightly out of balance.
I'm attaching also photos that can go in one corner.
Please do keep the color orange
Updates

Please I need the signage in Arial Fonts with colors Orange and Black & White for letters or combination
is up to You .

Thank You
Dorian

Colors
f37022

Requirements
Must have
• Clinical Hypnosis
- Weight Loss
- Fear of
Public Speaking
- Anxiety
- Depression
- PTS
- Stop Smoking
- Confidence Building
- Alcohol Moderation

Book now: www.calmtidetrance.net
or call 9462 3089
Should not have
• do You guys see the letters on the signage? "Harbor Sparrows" if You can do the that with Weight Loss ,Stop Smoking, Fear Of Public Speaking , Alcohol Moderation . The letters a bit out of balance .

```html
<!DOCTYPE html>
<html lang="en">
<head>
<meta charset="utf-8">
<title>Clinical Hypnosis Signage</title>
<link rel="stylesheet" href="https://fonts.googleapis.com/css2?family=Arimo:wght@400;700&display=swap">
<style>
  :root {
    --orange: #f37022;
    --orange-deep: #e4601a;
    --ink: #1d1d1d;
    --ink-soft: #333333;
    --paper: #ffffff;
    --paper-shade: #e6e6e6;
    --backdrop: #ececec;
    --rule: #5a5a5a;
  }
  * { box-sizing: border-box; margin: 0; padding: 0; }
  html, body {
    width: 1200px;
    height: 900px;
    overflow: hidden;
    background: var(--backdrop);
    font-family: "Arimo", Arial, sans-serif;
  }
  .canvas {
    position: relative;
    width: 1200px;
    height: 900px;
  }
  .sign {
    position: absolute;
    left: 40px;
    top: 194px;
    width: 1120px;
    height: 512px;
    overflow: hidden;
    background: linear-gradient(180deg, var(--paper) 0%, var(--paper) 60%, var(--paper-shade) 100%);
    box-shadow: 0 6px 18px rgba(0,0,0,0.18);
  }
  .sign-art {
    position: absolute;
    inset: 0;
    width: 1120px;
    height: 512px;
  }
  .sign-title {
    position: absolute;
    right: 52px;
    top: 62px;
    text-align: right;
    color: var(--orange);
    font-weight: 700;
    font-size: 52px;
    line-height: 1.06;
    letter-spacing: 0.5px;
  }
  .service-list {
    position: absolute;
    list-style: none;
    color: var(--ink-soft);
    font-size: 24px;
    line-height: 36px;
  }
  .service-list li::before {
    content: "";
    display: inline-block;
    width: 8px;
    height: 8px;
    border-radius: 50%;
    background: var(--ink);
    margin-right: 12px;
    vertical-align: middle;
    position: relative;
    top: -2px;
  }
  .service-list--primary { left: 568px; top: 214px; }
  .service-list--secondary { left: 866px; top: 206px; }
  .contact-rule {
    position: absolute;
    left: 0;
    right: 0;
    top: 398px;
    height: 2px;
    background: var(--rule);
  }
  .contact-line {
    position: absolute;
    left: 34px;
    right: 30px;
    top: 418px;
    color: var(--ink);
    font-size: 46px;
    letter-spacing: 0.6px;
    white-space: nowrap;
  }
</style>
</head>
<body>
<div class="canvas">
  <section class="sign">
    <svg class="sign-art" viewBox="0 0 1120 512" aria-hidden="true">
      <defs>
        <linearGradient id="couple-tones" x1="0" y1="0" x2="1" y2="0">
          <stop offset="0" stop-color="#8f9a4e"/>
          <stop offset="0.18" stop-color="#d8c6a6"/>
          <stop offset="0.45" stop-color="#e9cdb6"/>
          <stop offset="0.7" stop-color="#f6d7c3"/>
          <stop offset="1" stop-color="#f37022"/>
        </linearGradient>
        <radialGradient id="portrait-tones" cx="0.5" cy="0.5" r="0.6">
          <stop offset="0" stop-color="#4a4a4a"/>
          <stop offset="1" stop-color="#101010"/>
        </radialGradient>
      </defs>
      <!-- orange header band -->
      <path d="M500 0 H1120 V46 C930 40 760 110 620 200 C560 238 520 262 460 290 L420 0 Z" fill="var(--orange)"/>
      <!-- white sweep along the header -->
      <path d="M1110 38 C920 30 760 96 620 190 C580 216 545 238 500 262" fill="none" stroke="var(--paper)" stroke-width="10" stroke-linecap="round"/>
    </svg>

    <svg class="sign-art" viewBox="0 0 1120 512" role="img" aria-label="Photo of a smiling mature couple embracing outdoors, fading into orange">
      <path d="M36 0 H740 C700 40 660 60 620 100 C580 150 540 220 470 290 C340 300 180 296 36 300 Z" fill="url(#couple-tones)"/>
      <path d="M36 300 C180 292 300 282 430 270 L36 318 Z" fill="#c9d4e6"/>
    </svg>

    <svg class="sign-art" viewBox="0 0 1120 512" role="img" aria-label="Black and white portrait of a troubled man in an orange oval frame">
      <ellipse cx="382" cy="344" rx="132" ry="84" fill="url(#portrait-tones)" stroke="var(--orange)" stroke-width="9"/>
    </svg>

    <h1 class="sign-title">Clinical<br>Hypnosis</h1>

    <ul class="service-list service-list--primary">
      <li>Weight Loss</li>
      <li>Fear of Public Speaking</li>
      <li>Anxiety</li>
      <li>Depression</li>
    </ul>
    <ul class="service-list service-list--secondary">
      <li>PTS</li>
      <li>Stop Smoking</li>
      <li>Confidence Building</li>
      <li>Alcohol Moderation</li>
    </ul>

    <div class="contact-rule"></div>
    <p class="contact-line">www.calmtidetrance.net or call 9462 3089</p>
  </section>
</div>
</body>
</html>
```